business cards

we want our logos on the back
the information on it are on the design I've uploaded
come up with whatever you think is best, we want something professional, sophisticated and sleek.

```html
<!DOCTYPE html>
<html lang="en">
<head>
<meta charset="utf-8">
<title>Vantage Health and Performance – Business Cards</title>
<link href="https://fonts.googleapis.com/css2?family=Roboto:wght@300;400;700&family=Montserrat:wght@300;400&display=swap" rel="stylesheet">
<style>
  :root {
    --stage: #232324;
    --green: #55b84a;
    --green-deep: #3f9c3a;
    --ink: #212025;
    --white: #ffffff;
    --shadow: rgba(0,0,0,0.55);
  }
  * { margin: 0; padding: 0; box-sizing: border-box; }
  html, body {
    width: 1200px; height: 711px; overflow: hidden;
    background: var(--stage);
  }
  .stage {
    position: relative; width: 1200px; height: 711px;
    display: flex; align-items: center; justify-content: center; gap: 44px;
  }
  .card {
    position: relative; width: 540px; height: 309px;
    border-radius: 3px; overflow: hidden;
    box-shadow: 0 14px 30px var(--shadow);
  }

  /* Front */
  .card--front { background: var(--green); }
  .front-brand {
    position: absolute; right: 34px; bottom: 34px;
    display: flex; align-items: center; gap: 10px;
  }
  .brand-square { width: 16px; height: 16px; background: var(--white); }
  .brand-name {
    font-family: "Montserrat", sans-serif; font-weight: 300;
    color: var(--white); letter-spacing: 0.32em; font-size: 17px;
    text-transform: uppercase; line-height: 1;
  }
  .front-tagline {
    position: absolute; right: 34px; bottom: 18px;
    font-family: "Montserrat", sans-serif; font-weight: 300;
    color: var(--white); font-size: 6px; letter-spacing: 0.08em;
    text-transform: uppercase;
  }

  /* Back */
  .card--back { background: var(--ink); display: flex; }
  .back-band {
    position: relative; width: 140px; height: 100%;
    background: var(--green); flex: none;
  }
  .band-brand {
    position: absolute; left: 50%; top: 50%;
    width: 290px;
    transform: translate(-50%, -50%) rotate(90deg);
    display: flex; flex-direction: column; align-items: flex-start; gap: 10px;
  }
  .band-brand-row { display: flex; align-items: center; gap: 12px; }
  .band-brand .brand-square { width: 20px; height: 20px; }
  .band-brand .brand-name { font-size: 26px; letter-spacing: 0.3em; }
  .band-tagline {
    font-family: "Montserrat", sans-serif; font-weight: 300;
    color: var(--white); font-size: 7px; letter-spacing: 0.08em;
    text-transform: uppercase; padding-left: 32px;
  }

  .back-details {
    flex: 1; padding: 32px 30px 26px 20px;
    display: flex; flex-direction: column; align-items: flex-end;
    text-align: right; font-family: "Roboto", sans-serif; color: var(--white);
  }
  .person-name {
    font-size: 27px; color: var(--green); font-weight: 400; line-height: 1.1;
    margin-bottom: 4px;
  }
  .person-name .given { font-weight: 700; }
  .person-role { font-size: 11.5px; font-weight: 400; line-height: 1.3; text-transform: uppercase; }
  .person-quals { font-size: 11.5px; font-weight: 400; line-height: 1.3; }
  .contact-list { list-style: none; margin-top: 22px; }
  .contact-item {
    display: flex; align-items: center; justify-content: flex-end; gap: 8px;
    font-size: 11.5px; line-height: 1.55;
  }
  .contact-icon { width: 12px; height: 12px; flex: none; }
  .contact-icon--none { visibility: hidden; }
  .contact-email { margin-top: 22px; font-size: 11.5px; }
</style>
</head>
<body>
<main class="stage">

  <section class="card card--front" aria-label="Business card front">
    <div class="front-brand">
      <span class="brand-square"></span>
      <span class="brand-name">Vantage</span>
    </div>
    <p class="front-tagline">Physio · S&amp;C · Coaching · Personal Training · Rehab · Recovery</p>
  </section>

  <section class="card card--back" aria-label="Business card back">
    <div class="back-band">
      <div class="band-brand">
        <div class="band-brand-row">
          <span class="brand-square"></span>
          <span class="brand-name">Vantage</span>
        </div>
        <p class="band-tagline">Physio · S&amp;C · Coaching · Personal Training · Rehab · Recovery</p>
      </div>
    </div>

    <div class="back-details">
      <h1 class="person-name"><span class="given">Daniel</span> Marlowe</h1>
      <p class="person-role">Director</p>
      <p class="person-role">Senior Physiotherapist</p>
      <p class="person-quals">BHlthSc, MPhysioPrac, MExSc(S&amp;C)</p>
      <p class="person-quals">ASCA Level 2</p>

      <ul class="contact-list">
        <li class="contact-item">27 Harlow St, Kensington Park
          <svg class="contact-icon contact-icon--none" viewBox="0 0 12 12"></svg>
        </li>
        <li class="contact-item">03 9555 0148
          <svg class="contact-icon" viewBox="0 0 12 12" aria-label="Phone"><path fill="#55b84a" d="M2.4 1l2 2.2-1 1.2c.7 1.5 1.8 2.6 3.2 3.3l1.2-1 2.2 2-1 1.8C5.6 10.3 1.7 6.4 1 2z"/></svg>
        </li>
        <li class="contact-item">03 9555 0193
          <svg class="contact-icon" viewBox="0 0 12 12" aria-label="Fax"><rect x="3" y="1" width="6" height="3" fill="none" stroke="#55b84a"/><rect x="1" y="4.5" width="10" height="6" rx="1" fill="#55b84a"/><rect x="3" y="6.5" width="6" height="1" fill="#212025"/></svg>
        </li>
      </ul>
      <p class="contact-item contact-email">dan@vantagehealthperformance.com.au
        <svg class="contact-icon" viewBox="0 0 12 12" aria-label="Email"><rect x="1" y="2.5" width="10" height="7" fill="#55b84a"/><path d="M1 2.5l5 4 5-4" fill="none" stroke="#212025" stroke-width="1"/></svg>
      </p>
    </div>
  </section>

</main>
</body>
</html>
```